Breezeway Comfort business cards design

Need a business card design for a Heating and Air Conditioning business. I need these items included.
Business name: Breezeway Comfort
Owner: Marcus Tollefsen
License # 2874590
Phone number # 555-382-4071
Email: breezewaycomfortair@mailvista.example
Sales
Service
Installation
Maintenance

Heating and Air Conditioning

Requirements
Must have
• Company name , license number , phone number , email

```html
<!DOCTYPE html>
<html lang="en">
<head>
<meta charset="utf-8">
<title>Breezeway Comfort — Business Cards</title>
<link rel="stylesheet" href="https://fonts.googleapis.com/css2?family=Montserrat:wght@400;500;600;700;800&display=swap">
<style>
  :root {
    --brand-blue: #1f5fae;
    --brand-blue-dark: #174a8a;
    --brand-orange: #e8562a;
    --ink: #2a3a52;
    --paper: #ffffff;
    --backdrop: #e9eaec;
  }
  * { box-sizing: border-box; margin: 0; padding: 0; }
  html, body { width: 798px; height: 1200px; overflow: hidden; }
  body {
    background: var(--backdrop);
    font-family: "Montserrat", sans-serif;
    color: var(--ink);
    position: relative;
  }
  .card {
    position: absolute;
    left: 79px;
    width: 640px;
    height: 366px;
    background: var(--paper);
    box-shadow: 0 10px 28px rgba(30, 40, 60, 0.14);
    overflow: hidden;
  }
  .card--front { top: 194px; }
  .card--back { top: 640px; }

  /* Front */
  .front-decor {
    position: absolute;
    top: 0; left: 0;
    width: 250px; height: 100%;
    background: linear-gradient(135deg, var(--brand-blue) 0%, var(--brand-blue-dark) 45%, rgba(31, 95, 174, 0) 100%);
  }
  .brand {
    position: absolute;
    left: 268px;
    top: 146px;
    display: flex;
    align-items: center;
    gap: 12px;
  }
  .brand__mark {
    flex: 0 0 auto;
    width: 36px; height: 36px;
    border-radius: 50%;
    background: var(--brand-orange);
  }
  .brand__name {
    font-weight: 800;
    font-size: 24px;
    letter-spacing: 0.4px;
    color: var(--brand-blue);
    text-transform: uppercase;
    line-height: 1;
    white-space: nowrap;
  }
  .brand__tagline {
    font-size: 9px;
    font-weight: 600;
    letter-spacing: 1.6px;
    color: var(--brand-blue);
    text-transform: uppercase;
    margin-top: 6px;
    white-space: nowrap;
  }
  .services {
    position: absolute;
    left: 268px;
    bottom: 54px;
    font-size: 10px;
    font-weight: 600;
    letter-spacing: 1.3px;
    color: var(--brand-blue);
    text-transform: uppercase;
    white-space: nowrap;
  }

  /* Back */
  .back-band {
    position: absolute;
    top: 0; right: 0;
    width: 150px; height: 100%;
    background: var(--brand-blue);
  }
  .owner {
    position: absolute;
    top: 34px;
    right: 180px;
    color: var(--brand-blue);
  }
  .owner__name {
    font-size: 17px;
    font-weight: 600;
    letter-spacing: 1.6px;
    text-transform: uppercase;
  }
  .owner__role, .owner__license {
    font-size: 10px;
    font-weight: 500;
    letter-spacing: 1.4px;
    text-transform: uppercase;
    margin-top: 4px;
  }
  .contact {
    position: absolute;
    left: 34px;
    bottom: 40px;
    color: var(--brand-blue);
  }
  .contact__rule {
    width: 440px;
    height: 1.5px;
    background: var(--brand-blue);
    margin-bottom: 14px;
  }
  .contact__phone {
    font-size: 28px;
    font-weight: 600;
    letter-spacing: 1px;
  }
  .contact__email {
    font-size: 10.5px;
    font-weight: 500;
    letter-spacing: 0.6px;
    margin-top: 6px;
  }
</style>
</head>
<body>

<section class="card card--front" aria-label="Business card front">
  <div class="front-decor" role="img" aria-label="Decorative blue sweeping airflow stripes"></div>
  <div class="brand">
    <span class="brand__mark" aria-hidden="true"></span>
    <div>
      <p class="brand__name">Breezeway Comfort</p>
      <p class="brand__tagline">Heating and Air Conditioning</p>
    </div>
  </div>
  <p class="services">Sales • Service • Installation • Maintenance</p>
</section>

<section class="card card--back" aria-label="Business card back">
  <div class="back-band" aria-hidden="true"></div>
  <div class="owner">
    <p class="owner__name">Marcus Tollefsen</p>
    <p class="owner__role">Owner</p>
    <p class="owner__license">License: 2874590</p>
  </div>
  <div class="contact">
    <div class="contact__rule" aria-hidden="true"></div>
    <p class="contact__phone">PHONE: 555-382-4071</p>
    <p class="contact__email">breezewaycomfortair@mailvista.example</p>
  </div>
</section>

</body>
</html>
```